Business Card Design

We are a General Practice - Family medicine
We also have Allied Health professionals working within our team

Industry/Entity Type

Business

Contact Information for Business Card

Front of the card to display:

BRAMBLEWICK MEDICAL
PHONE 6348 2917

5/41 Fennimore Parade
Launceston Tasmania 7284

Back of the card to display:

My Appointments
Date:
Time:
With:

Please remember to phone us on 6348 2917 to cancel your appointment if you can't keep it.
A fee applied to missed appointments

```html
<!DOCTYPE html>
<html lang="en">
<head>
<meta charset="utf-8">
<title>Bramblewick Medical – Business Card</title>
<link rel="stylesheet" href="https://fonts.googleapis.com/css2?family=Fira+Sans:ital,wght@0,400;0,500;1,400&display=swap">
<style>
  :root {
    --page-bg: #f2f4f6;
    --card-white: #ffffff;
    --brand-blue: #2ea7df;
    --brand-blue-soft: #8fd0f0;
    --brand-green: #8dc63f;
    --brand-green-dark: #7ab52f;
    --ink: #15202b;
    --white: #ffffff;
    --dots: rgba(255,255,255,0.85);
  }
  * { box-sizing: border-box; margin: 0; padding: 0; }
  html, body { width: 1200px; height: 1040px; overflow: hidden; }
  body {
    background: var(--page-bg);
    font-family: "Fira Sans", Arial, sans-serif;
    position: relative;
  }
  .card {
    position: absolute;
    left: 260px;
    width: 680px;
    height: 420px;
    overflow: hidden;
    box-shadow: 0 3px 10px rgba(0,0,0,0.25);
  }
  .card--front { top: 60px; background: var(--card-white); }
  .card--back { top: 560px; background: var(--brand-green); }

  /* Front */
  .front__accent {
    position: absolute; right: -90px; top: -110px;
    width: 330px; height: 330px; border-radius: 50%;
    background: radial-gradient(circle at 40% 60%, var(--brand-blue-soft), var(--brand-blue));
    opacity: 0.85;
  }
  .brand {
    position: absolute; left: 40px; top: 112px;
    display: flex; align-items: center; gap: 12px;
  }
  .brand__dot { width: 22px; height: 22px; border-radius: 50%; background: var(--brand-green); }
  .brand__name { font-size: 32px; font-weight: 400; color: var(--brand-blue); }
  .front__band {
    position: absolute; left: 0; right: 0; top: 222px; bottom: 0;
    background: var(--brand-blue);
    border-top: 3px solid var(--brand-green);
    text-align: center;
  }
  .front__name { margin-top: 10px; font-size: 30px; color: var(--white); font-weight: 400; }
  .front__phone {
    margin-top: 4px; font-size: 31px; color: var(--ink);
    display: flex; justify-content: center; align-items: center; gap: 6px;
  }
  .front__phone svg { width: 22px; height: 22px; }
  .front__address { margin-top: 34px; font-size: 28px; color: var(--ink); }

  /* Back */
  .back__mark {
    position: absolute; left: 265px; top: 140px;
    width: 150px; height: 150px; border-radius: 50%;
    background: var(--brand-green-dark); opacity: 0.6;
  }
  .back__title {
    position: absolute; left: 0; right: 0; top: 34px; height: 36px;
    background: var(--brand-blue); color: var(--white);
    font-size: 26px; text-align: center; line-height: 36px;
  }
  .fields { position: absolute; left: 39px; top: 92px; width: 400px; }
  .field {
    display: flex; align-items: flex-end; height: 30px; margin-bottom: 30px;
    font-size: 22px; color: var(--ink);
  }
  .field__line { flex: 1; border-bottom: 1px dotted var(--dots); margin-left: 2px; margin-bottom: 4px; }
  .back__note {
    position: absolute; left: 56px; top: 284px; width: 580px;
    font-size: 17.5px; line-height: 24px; color: var(--ink);
  }
  .back__note .phone { color: var(--white); }
  .back__fee {
    position: absolute; left: 0; right: 0; top: 348px; height: 34px;
    background: var(--brand-blue); color: var(--white);
    font-size: 18px; font-style: italic; text-align: center; line-height: 34px;
  }
</style>
</head>
<body>
  <section class="card card--front" aria-label="Card front">
    <div class="front__accent"></div>
    <div class="brand">
      <span class="brand__dot"></span>
      <span class="brand__name">Bramblewick Medical</span>
    </div>
    <div class="front__band">
      <p class="front__name">BRAMBLEWICK MEDICAL</p>
      <p class="front__phone">
        <svg viewBox="0 0 24 24" aria-hidden="true"><path fill="#ffffff" d="M6.6 10.8c1.4 2.8 3.8 5.1 6.6 6.6l2.2-2.2c.3-.3.7-.4 1-.2 1.1.4 2.3.6 3.6.6.6 0 1 .4 1 1V20c0 .6-.4 1-1 1C10.6 21 3 13.4 3 4c0-.6.4-1 1-1h3.5c.6 0 1 .4 1 1 0 1.3.2 2.5.6 3.6.1.3 0 .7-.2 1L6.6 10.8z"/></svg>
        6348 2917
      </p>
      <p class="front__address">5/41 Fennimore Parade, Launceston Tasmania 7284</p>
    </div>
  </section>

  <section class="card card--back" aria-label="Card back">
    <div class="back__mark"></div>
    <h2 class="back__title" style="font-weight:400">My Appointments</h2>
    <div class="fields">
      <div class="field">Date:<span class="field__line"></span></div>
      <div class="field">Time:<span class="field__line"></span></div>
      <div class="field">With:<span class="field__line"></span></div>
    </div>
    <p class="back__note">Please remember to phone us on <span class="phone">6348 2917</span> to cancel your appointment if you can't keep it.</p>
    <p class="back__fee">A fee applied to missed appointments</p>
  </section>
</body>
</html>
```